Two Separate Canvas Posters 54"width x 36" Height

I need two (2) posters designed for a new restaurant concept called: Lumaro Fresh Pita Grill.
Both posters will be printed on Canvas and placed into our new restaurants dining area.
I want this to look hip and cool.
I want so see red colors and earth tones. Please see attached for some ideas that I have.
The final design should communicate that you really gotta have this product and that this is a fun and casual place for a quick bite on the go.
Poster 1 message: gotta Eatta pita!
Size: 54"width x 36" high
Idea: Please see attached for design ideas and colors that I would like to see. If you can come up with any better idea, I would love to see this.
Poster 2 message: Power to the Pita
Size: 54"width x 36" height
Idea: Please see attached for design idea and colors that I want to see.
Restaurant

```html
<!DOCTYPE html>
<html lang="en">
<head>
<meta charset="utf-8">
<title>Lumaro Fresh Pita Grill – gotta Eatta pita!</title>
<link href="https://fonts.googleapis.com/css2?family=Didact+Gothic&display=swap" rel="stylesheet">
<style>
  :root {
    --page: #ffffff;
    --red-deep: #c9222a;
    --red: #e0302b;
    --vermilion: #ea4b26;
    --orange: #f07a2a;
    --amber: #f5a03a;
    --gold: #f8bf5a;
    --sand: #fbd89a;
    --rust: #9e2f1c;
    --headline: rgba(255, 242, 228, 0.88);
    --badge: rgba(255, 255, 255, 0.78);
    --brand-green: #2e9a3a;
  }
  * { margin: 0; padding: 0; box-sizing: border-box; }
  html, body {
    width: 1200px;
    height: 886px;
    overflow: hidden;
    background: var(--page);
  }
  .poster {
    position: absolute;
    left: 22px;
    top: 61px;
    width: 1159px;
    height: 773px;
    overflow: hidden;
    font-family: "Didact Gothic", "Century Gothic", sans-serif;
    background: linear-gradient(90deg,
      var(--vermilion) 0 2%, var(--red) 2% 4%, var(--orange) 4% 6%,
      var(--amber) 6% 7%, var(--red) 7% 9%, var(--vermilion) 9% 12%,
      var(--amber) 12% 13.5%, var(--red-deep) 13.5% 16%, var(--red) 16% 18%,
      var(--orange) 18% 20%, var(--gold) 20% 21%, var(--vermilion) 21% 24%,
      var(--amber) 24% 26%, var(--orange) 26% 28%, var(--red) 28% 30%,
      var(--gold) 30% 32%, var(--amber) 32% 34%, var(--sand) 34% 36%,
      var(--gold) 36% 38%, var(--orange) 38% 40%, var(--sand) 40% 42%,
      var(--amber) 42% 44%, var(--gold) 44% 46%, var(--orange) 46% 48%,
      var(--amber) 48% 50%, var(--red) 50% 52%, var(--orange) 52% 54%,
      var(--sand) 54% 56%, var(--vermilion) 56% 58%, var(--amber) 58% 60%,
      var(--red) 60% 62%, var(--orange) 62% 64%, var(--vermilion) 64% 66%,
      var(--gold) 66% 67.5%, var(--red-deep) 67.5% 70%, var(--orange) 70% 72%,
      var(--amber) 72% 74%, var(--red) 74% 76%, var(--vermilion) 76% 78%,
      var(--orange) 78% 80%, var(--red-deep) 80% 82%, var(--amber) 82% 84%,
      var(--red) 84% 86%, var(--orange) 86% 88%, var(--vermilion) 88% 90%,
      var(--red-deep) 90% 92%, var(--amber) 92% 94%, var(--red) 94% 96%,
      var(--vermilion) 96% 98%, var(--red-deep) 98% 100%);
  }
  .poster::after {
    content: "";
    position: absolute;
    inset: 0;
    background: radial-gradient(ellipse 55% 60% at 100% 100%, rgba(110, 30, 15, 0.55), transparent 70%);
    pointer-events: none;
  }
  .headline {
    position: absolute;
    inset: 0;
    z-index: 1;
    color: var(--headline);
    font-weight: 400;
  }
  .headline__line {
    position: absolute;
    display: block;
    font-size: 200px;
    line-height: 1;
    letter-spacing: -2px;
    white-space: nowrap;
  }
  .headline__line--gotta { left: 380px; top: 166px; }
  .headline__line--eatta { left: 684px; top: 356px; }
  .headline__line--pita  { left: 550px; top: 504px; }
  .brand-badge {
    position: absolute;
    z-index: 1;
    left: 0;
    top: 561px;
    width: 288px;
    height: 111px;
    background: var(--badge);
    display: flex;
    align-items: center;
    justify-content: center;
  }
  .brand-badge__name {
    font-size: 52px;
    line-height: 1;
    color: var(--brand-green);
    font-weight: 400;
  }
</style>
</head>
<body>
  <main class="poster">
    <h1 class="headline">
      <span class="headline__line headline__line--gotta">gotta</span>
      <span class="headline__line headline__line--eatta">Eatta</span>
      <span class="headline__line headline__line--pita">pita!</span>
    </h1>
    <div class="brand-badge">
      <span class="brand-badge__name">Lumaro</span>
    </div>
  </main>
</body>
</html>
```